添付のパッケージサンプルを元にデザインお願いします。
箱ではなく真空袋なので、中央部分が膨らみます。
https://pshop.m48v.jp/sunadokei/cabinet/31862207/imgqx5520418396.jpg
贈り物で貰った時に、テンションが上がるようなデザインを希望。
シンプル 複雑
単色 カラフル
暗い 明るい
日常 高級
遊び心 厳粛
未来的 伝統的
女性的 男性的
茶系、無彩色系
• イラストレーター形式 (.ai)

デザイン性、インパクト

皆さんありがとうございました。

```html
<!DOCTYPE html>
<html lang="ja">
<head>
<meta charset="utf-8">
<title>焼さば寿司 パッケージ</title>
<link rel="stylesheet" href="https://fonts.googleapis.com/css2?family=Shippori+Mincho:wght@500;700&family=Yuji+Syuku&display=swap">
<style>
  :root {
    --paper: #e8e5de;
    --paper-light: #f1efe9;
    --ink: #1a1a1a;
    --ink-soft: #3a3a3a;
    --smoke-mid: #6d6d6b;
    --gold: #c1913f;
    --gold-light: #e3c27a;
    --gold-dark: #8c6424;
    --fish: #5d6e78;
  }
  html, body {
    margin: 0;
    padding: 0;
    width: 755px;
    height: 1200px;
    overflow: hidden;
    background: var(--paper);
  }
  .package {
    position: relative;
    width: 755px;
    height: 1200px;
    overflow: hidden;
    background: radial-gradient(ellipse at 50% 20%, var(--paper-light), var(--paper) 70%);
    font-family: "Shippori Mincho", serif;
  }
  .ink-smoke {
    position: absolute;
    left: 0;
    top: 420px;
    width: 755px;
    height: 780px;
    background:
      radial-gradient(ellipse 260px 160px at 30% 18%, rgba(40,40,40,0.85), rgba(40,40,40,0) 70%),
      radial-gradient(ellipse 300px 180px at 78% 24%, rgba(30,30,30,0.8), rgba(30,30,30,0) 70%),
      radial-gradient(ellipse 200px 120px at 55% 6%, rgba(110,110,108,0.5), rgba(110,110,108,0) 70%),
      linear-gradient(to bottom, rgba(26,26,26,0) 0%, rgba(26,26,26,0.75) 22%, var(--ink) 45%, var(--ink) 100%);
  }
  .brand {
    position: absolute;
    left: 38px;
    top: 34px;
    display: flex;
    align-items: center;
    gap: 10px;
    color: var(--ink);
    font-weight: 700;
    font-size: 40px;
    letter-spacing: 2px;
  }
  .brand-mark {
    width: 14px;
    height: 14px;
    background: var(--ink);
  }
  .tagline {
    position: absolute;
    right: 190px;
    top: 110px;
    writing-mode: vertical-rl;
    color: var(--ink-soft);
    font-weight: 500;
    font-size: 50px;
    line-height: 1.55;
    letter-spacing: 6px;
    margin: 0;
  }
  .fish-illustration {
    position: absolute;
    left: 200px;
    top: 440px;
    width: 380px;
    height: 110px;
    border-radius: 55% 45% 45% 55% / 50%;
    background: linear-gradient(to bottom, var(--fish), #9aa8ae 55%, #d9dcdb);
  }
  .product-name {
    position: absolute;
    left: 50%;
    top: 600px;
    transform: translateX(-50%);
    writing-mode: vertical-rl;
    margin: 0;
    font-family: "Yuji Syuku", serif;
    font-weight: 400;
    font-size: 118px;
    letter-spacing: 2px;
    line-height: 1;
    background: linear-gradient(100deg, var(--gold-dark), var(--gold-light) 45%, var(--gold) 70%, var(--gold-dark));
    -webkit-background-clip: text;
    background-clip: text;
    color: transparent;
  }
</style>
</head>
<body>
  <main class="package">
    <div class="ink-smoke" role="img" aria-label="下部に広がる墨の煙のような背景"></div>

    <div class="brand">
      <span class="brand-mark"></span>
      <span class="brand-name">浜風組</span>
    </div>

    <p class="tagline">鯖好き県<br>からの<br>贈り物</p>

    <div class="fish-illustration" role="img" aria-label="横向きに泳ぐ鯖のイラスト"></div>

    <h1 class="product-name">焼さば寿司</h1>
  </main>
</body>
</html>
```